Solar Energy Technology Company - Solar Savings Analysis Flyer

I Have Included The Text Content I Want Put On An 8 1/2 " x 11" Flyer.

I Want To See It In One Page Format And In Tri-Fold Brochure Format.

It Needs To Grab And Captivate Prospective Customers, Awesome Graphics, Layout, Etc.

We Are A Cutting Edge Solar Energy Solutions & Technology Company.

We Need A World Class High Tech Look and Logo For Our Company Included On Our 8 1/2 x 11 Flyer & Trifold Brochure

Brightfold Venture Partners, LLC
"Forward Ideas Delivered"

Would Like A Black Gold And Electric Blue Color Scheme, However, We We Are Open To Seeing Your Creativity, Colors, Graphics Etc. For Consideration.

Target Market(s)

Homeowners Without Solar Panels On Their Roof

Industry/Entity Type

New Roof Top Solar Energy Producing Panel Technology Systems

Font styles to use
Serif

Requirements
Must have
• See My Attached Flyer/Trifold Brochure Display Content
Nice to have
• Gold Black And Electric Blue Color Scheme, Solar Theme Background Graphics

```html
<!DOCTYPE html>
<html lang="en">
<head>
<meta charset="utf-8">
<title>Brightfold Venture Partners – Solar Savings Flyer</title>
<link href="https://fonts.googleapis.com/css2?family=Montserrat:wght@400;600;700;800;900&family=Oswald:wght@500;600;700&display=swap" rel="stylesheet">
<style>
  :root {
    --electric-blue: #1f4fe0;
    --deep-blue: #143aa8;
    --gold: #c9962e;
    --gold-light: #e2b64f;
    --ink: #1b1d22;
    --charcoal: #2a2d33;
    --paper: #ffffff;
    --backdrop: #e6e6e4;
    --grey: #6d7079;
    --soft-grey: #eceef2;
  }
  * { box-sizing: border-box; margin: 0; padding: 0; }
  html, body { width: 784px; height: 1200px; overflow: hidden; }
  body {
    background: var(--backdrop);
    font-family: "Montserrat", Arial, sans-serif;
    color: var(--ink);
    position: relative;
  }
  .flyer {
    position: absolute; left: 12px; top: 108px;
    width: 760px; height: 984px;
    background: var(--paper);
    overflow: hidden;
    box-shadow: 0 4px 18px rgba(0,0,0,.18);
  }
  .abs { position: absolute; }

  /* header */
  .brand { left: 28px; top: 22px; display: flex; align-items: center; gap: 10px; }
  .brand-dot { width: 34px; height: 34px; border-radius: 50%; background: var(--gold); }
  .brand-name { font-weight: 800; font-size: 13px; color: var(--deep-blue); text-transform: uppercase; letter-spacing: .3px; line-height: 1.15; }
  .brand-tag { font-weight: 600; font-size: 9px; color: var(--deep-blue); margin-top: 2px; }

  .hero-shapes { left: 0; top: 0; width: 760px; height: 350px; }

  /* headline */
  .attention { left: 30px; top: 112px; color: var(--paper); font-family: "Oswald", sans-serif; font-weight: 600; font-size: 48px; line-height: 1; letter-spacing: .5px; }
  .fed-up { left: 30px; top: 222px; width: 380px; height: 64px; background: var(--paper); border: 2px solid var(--electric-blue); padding: 6px 14px; }
  .fed-up .q { font-weight: 700; font-size: 17px; color: var(--ink); }
  .fed-up .q-strong { font-weight: 900; font-size: 19px; color: var(--deep-blue); text-transform: uppercase; }

  /* offer row */
  .pay { left: 30px; top: 300px; width: 250px; height: 62px; background: var(--charcoal); color: var(--paper); padding: 6px 14px; }
  .pay .small { font-size: 11px; font-weight: 600; }
  .pay .amount { font-family: "Oswald", sans-serif; font-size: 32px; font-weight: 700; line-height: 1; }
  .lower { left: 286px; top: 300px; width: 270px; height: 62px; }
  .lower .top { background: var(--charcoal); color: var(--paper); font-size: 11px; font-weight: 600; padding: 5px 12px; height: 24px; }
  .lower .bottom { background: var(--gold); color: var(--paper); font-family: "Oswald", sans-serif; font-size: 23px; font-weight: 600; height: 38px; padding: 2px 12px; letter-spacing: .5px; }
  .cut-bill { left: 30px; top: 376px; font-weight: 800; font-size: 27px; color: var(--deep-blue); text-transform: uppercase; letter-spacing: .2px; }
  .cut-bill span { color: var(--gold); }

  /* feature row */
  .plug-photo { left: 30px; top: 426px; width: 220px; height: 96px; background: linear-gradient(135deg, #3a3d44, #8a8d94 55%, #c9c3b6); }
  .install-note { left: 262px; top: 426px; width: 230px; height: 96px; background: var(--soft-grey); border-left: 4px solid var(--electric-blue); padding: 12px 14px; font-size: 11.5px; font-weight: 600; line-height: 1.45; color: var(--charcoal); }
  .subsidy { left: 504px; top: 426px; width: 226px; height: 96px; }
  .subsidy .ask { font-size: 10px; font-weight: 700; color: var(--grey); text-transform: uppercase; padding: 4px 0 4px 2px; }
  .subsidy .gov { background: var(--gold); color: var(--paper); font-family: "Oswald", sans-serif; font-size: 26px; font-weight: 600; padding: 0 12px; height: 36px; line-height: 36px; }
  .subsidy .sub { background: var(--electric-blue); color: var(--paper); font-family: "Oswald", sans-serif; font-size: 26px; font-weight: 600; padding: 0 12px; height: 36px; line-height: 36px; }

  /* savings table */
  .savings-head { left: 0; top: 550px; width: 760px; text-align: center; font-weight: 800; font-size: 14px; text-transform: uppercase; color: var(--ink); }
  .savings-head span { color: var(--electric-blue); }
  .savings { left: 40px; top: 584px; width: 680px; display: flex; justify-content: space-between; }
  .tier { width: 120px; text-align: center; }
  .tier-bill { width: 78px; height: 78px; border-radius: 50%; margin: 0 auto; background: var(--charcoal); border: 4px solid var(--soft-grey); box-shadow: 0 0 0 2px var(--charcoal); color: var(--paper); font-family: "Oswald", sans-serif; font-size: 24px; font-weight: 600; line-height: 70px; }
  .tier-save { margin-top: 12px; background: var(--soft-grey); border-top: 4px solid var(--electric-blue); padding: 8px 4px 10px; }
  .tier-save .label { font-size: 9.5px; font-weight: 700; color: var(--grey); text-transform: uppercase; }
  .tier-save .value { font-family: "Oswald", sans-serif; font-size: 26px; font-weight: 700; color: var(--deep-blue); line-height: 1.1; }

  .fine { left: 40px; top: 790px; width: 680px; text-align: center; font-size: 12px; font-weight: 600; color: var(--charcoal); line-height: 1.5; }

  /* footer */
  .footer-stripe { left: 0; top: 876px; width: 760px; height: 10px; background: var(--electric-blue); }
  .footer { left: 0; top: 886px; width: 760px; height: 98px; background: var(--ink); color: var(--paper); display: flex; align-items: center; justify-content: space-between; padding: 0 30px; }
  .footer .cta { font-size: 13px; font-weight: 700; max-width: 420px; line-height: 1.4; }
  .footer .contact { text-align: right; }
  .footer .contact .co { font-size: 12px; font-weight: 800; color: var(--gold-light); text-transform: uppercase; }
  .footer .contact .phone { display: flex; align-items: center; justify-content: flex-end; gap: 6px; font-family: "Oswald", sans-serif; font-size: 22px; font-weight: 600; }
</style>
</head>
<body>
  <main class="flyer">
    <svg class="abs hero-shapes" viewBox="0 0 760 350" aria-hidden="false">
      <polygon points="540,0 760,0 760,60" fill="#1b1d22"/>
      <polygon points="400,0 560,0 470,120" fill="#c9962e"/>
      <g role="img" aria-label="Photo of a two-storey suburban house with a front lawn at dusk">
        <polygon points="470,120 560,0 760,0 760,350 560,350 620,200" fill="url(#house)"/>
      </g>
      <polygon points="0,100 560,100 500,210 0,210" fill="#1f4fe0"/>
      <polygon points="500,210 560,100 590,100 530,210" fill="#c9962e"/>
      <polygon points="560,350 620,200 640,200 585,350" fill="#1b1d22"/>
      <defs>
        <linearGradient id="house" x1="0" y1="0" x2="0" y2="1">
          <stop offset="0" stop-color="#7fa6d6"/>
          <stop offset=".55" stop-color="#5d6a80"/>
          <stop offset="1" stop-color="#4d6b3a"/>
        </linearGradient>
      </defs>
    </svg>

    <div class="abs brand">
      <div class="brand-dot"></div>
      <div>
        <div class="brand-name">Brightfold Venture Partners, LLC</div>
        <div class="brand-tag">"Forward Ideas Delivered"</div>
      </div>
    </div>

    <h1 class="abs attention">ATTENTION<br>HOMEOWNER!</h1>

    <div class="abs fed-up">
      <div class="q">Are You FED UP With</div>
      <div class="q-strong">Your High Electric Bills?</div>
    </div>

    <div class="abs pay">
      <div class="small">We Will Pay You</div>
      <div class="amount">$2,000...</div>
    </div>
    <div class="abs lower">
      <div class="top">When You Allow Us To Make Your Electric Bill</div>
      <div class="bottom">PERMANENTLY LOWER</div>
    </div>

    <div class="abs cut-bill">Your Electric Bill By At Least <span>25% To 50%!</span></div>

    <div class="abs plug-photo" role="img" aria-label="Photo of a hand holding an electrical plug"></div>
    <p class="abs install-note">No money out of pocket. Our certified team designs and installs panels built for your roof.</p>
    <div class="abs subsidy">
      <div class="ask">Ask about available programs</div>
      <div class="gov">GOVERNMENT</div>
      <div class="sub">SUBSIDIZED!</div>
    </div>

    <h2 class="abs savings-head">If Your Last 12 Months' <span>Average Monthly Electric Payment</span> Is:</h2>

    <div class="abs savings">
      <div class="tier"><div class="tier-bill">$100</div><div class="tier-save"><div class="label">Monthly Savings:</div><div class="value">$67</div></div></div>
      <div class="tier"><div class="tier-bill">$200</div><div class="tier-save"><div class="label">Monthly Savings:</div><div class="value">$134</div></div></div>
      <div class="tier"><div class="tier-bill">$300</div><div class="tier-save"><div class="label">Monthly Savings:</div><div class="value">$201</div></div></div>
      <div class="tier"><div class="tier-bill">$400</div><div class="tier-save"><div class="label">Monthly Savings:</div><div class="value">$268</div></div></div>
      <div class="tier"><div class="tier-bill">$500</div><div class="tier-save"><div class="label">Monthly Savings:</div><div class="value">$335</div></div></div>
    </div>

    <p class="abs fine">If your average is above $500, call us today. Savings grow higher with every bill.<br>Our free analysis shows exactly what you keep each month.</p>

    <div class="abs footer-stripe"></div>
    <footer class="abs footer">
      <div class="cta">Schedule your free solar savings analysis today and start saving.</div>
      <div class="contact">
        <div class="co">Brightfold Venture Partners, LLC</div>
        <div class="phone">
          <svg width="18" height="18" viewBox="0 0 24 24" aria-hidden="true"><path fill="#e2b64f" d="M6.6 10.8a15.1 15.1 0 0 0 6.6 6.6l2.2-2.2a1 1 0 0 1 1-.25 11.4 11.4 0 0 0 3.6.57 1 1 0 0 1 1 1V20a1 1 0 0 1-1 1A17 17 0 0 1 3 4a1 1 0 0 1 1-1h3.5a1 1 0 0 1 1 1c0 1.25.2 2.45.57 3.6a1 1 0 0 1-.25 1z"/></svg>
          Call (555) 014-2783
        </div>
      </div>
    </footer>
  </main>
</body>
</html>
```